Brellmoor Cosmetic Doctor is the title and the name of the business

Facebook advertising: keep
To those dimensions

Aimed at Caucasian women between the ages of 18 - 60 interested in beauty and cosmetic injectables. Will be boosted on facebook which is my advertising platform.

Name: Brellmoor Cosmetic Doctor
0400 555 271

Forehead $58
Frown lines $116
Crows feet $116
Lip fillers $380

I would like to have a beautiful girl that suits the picture.

Target Market(s)

Females between 18 - 60 interested in Lumarex and cosmetic fillers
Prefer Caucasian as that's the majority of population

Industry/Entity Type

Beauty Salon

Font styles to use
Serif
Script

Colors
e667a6
eea4c8
f9d9e8
fee18a
fbf289
fbee3d
cadf82
cedeed
85cae6

Requirements
Must have
• Name: Brellmoor Cosmetic Doctor
• Phone number: 0400 559 271
• Prices:
• Forehead $58
• Frown lines $116
• Crows feet $116
• Lip fillers $380
• Picture of female that is very beautiful
Nice to have
• Not a cartoon or anything else that's not a real picture of a female
Should not have
• No cartoon pictures. Proper picture of women

```html
<!DOCTYPE html>
<html lang="en">
<head>
<meta charset="utf-8">
<title>Brellmoor Cosmetic Doctor – Ad Sizes</title>
<link rel="stylesheet" href="https://fonts.googleapis.com/css2?family=Parisienne&family=Cinzel:wght@400;600&family=PT+Sans:wght@700&display=swap">
<style>
  :root {
    --stage: #000000;
    --size-label: #ffffff;
    --panel-white: #ffffff;
    --panel-grey: #ebebeb;
    --ink: #4a2a26;
    --card-fill: #fdefe3;
    --card-line: #8c8180;
    --blush: #f9d9e8;
    --rose: #eea4c8;
    --skin-light: #f3e1d6;
    --skin-mid: #e4c3b0;
    --hair: #b89a7c;
  }
  * { box-sizing: border-box; margin: 0; padding: 0; }
  html, body { width: 1200px; height: 1200px; overflow: hidden; background: var(--stage); }
  .stage { position: relative; width: 1200px; height: 1200px; }

  .size-label {
    position: absolute; color: var(--size-label);
    font: 600 22px/1 "PT Sans", sans-serif; transform: translateX(-50%);
    white-space: nowrap;
  }

  .ad { position: absolute; overflow: hidden; background: var(--panel-white); }
  .ad > * { position: absolute; }

  .model-photo {
    background: linear-gradient(160deg, var(--panel-white) 0%, var(--skin-light) 40%, var(--skin-mid) 75%, var(--hair) 100%);
  }

  .brand-title {
    left: 0; right: 0; text-align: center; color: var(--ink);
    font-family: "Parisienne", cursive; line-height: 1.05; z-index: 2;
  }
  .brand-line { display: block; }

  .offer-text, .prices-heading, .contact-phone, .contact-address {
    text-align: center; color: var(--ink); font-family: "Cinzel", serif; z-index: 2;
  }
  .offer-text { text-transform: uppercase; line-height: 1.25; }
  .prices-heading { text-transform: uppercase; }

  .price-card {
    display: flex; flex-direction: column; align-items: center; justify-content: center;
    color: var(--ink); z-index: 2;
  }
  .card-frame { position: absolute; inset: 0; width: 100%; height: 100%; }
  .treatment {
    position: relative; font-family: "PT Sans", sans-serif; font-weight: 700;
    border-bottom: 4px double var(--ink); padding: 0 2px 3px;
  }
  .price { position: relative; font-family: "PT Sans", sans-serif; font-weight: 700; line-height: 1.1; }

  /* tall 504 x 1200 */
  .ad-tall { left: 107px; top: 138px; width: 403px; height: 960px; background: linear-gradient(180deg, var(--panel-white) 0 60%, var(--panel-grey) 100%); }
  .ad-tall .header-band { left: 0; top: 0; width: 100%; height: 102px; background: var(--panel-grey); }
  .ad-tall .brand-title { top: 12px; font-size: 38px; }
  .ad-tall .model-photo { left: 0; top: 102px; width: 100%; height: 360px; }
  .ad-tall .offer-text { left: 20px; right: 20px; top: 478px; font-size: 13.5px; }
  .ad-tall .offer-text span { display: block; margin-bottom: 8px; }
  .ad-tall .prices-heading { left: 0; right: 0; top: 566px; font-size: 13px; }
  .ad-tall .treatment { font-size: 17px; }
  .ad-tall .price { font-size: 41px; margin-top: 6px; }
  .ad-tall .contact-phone { left: 0; right: 0; top: 901px; font-size: 23px; }
  .ad-tall .contact-address { left: 0; right: 0; top: 931px; font-size: 11px; }

  /* medium 600 x 600 */
  .ad-medium { left: 613px; top: 176px; width: 479px; height: 479px; }
  .ad-medium .model-photo { left: 227px; top: 0; width: 252px; height: 100%; }
  .ad-medium .brand-title { top: 28px; right: 190px; font-size: 31px; }
  .ad-medium .offer-text { left: 0; right: 190px; top: 106px; font-size: 10px; line-height: 1.2; }
  .ad-medium .prices-heading { left: 0; right: 190px; top: 137px; font-size: 10px; }
  .ad-medium .treatment { font-size: 15px; }
  .ad-medium .price { font-size: 36px; margin-top: 4px; }
  .ad-medium .contact-phone { left: 0; right: 190px; top: 422px; font-size: 21px; }
  .ad-medium .contact-address { left: 0; right: 190px; top: 450px; font-size: 10.5px; }

  /* small 400 x 400 */
  .ad-small { left: 692px; top: 752px; width: 320px; height: 318px; }
  .ad-small .model-photo { left: 213px; top: 0; width: 107px; height: 100%; }
  .ad-small .brand-title { top: 12px; right: 110px; font-size: 22px; }
  .ad-small .offer-text { left: 0; right: 110px; top: 58px; font-size: 8.5px; line-height: 1.35; }
  .ad-small .prices-heading { left: 0; right: 110px; top: 88px; font-size: 8.5px; }
  .ad-small .treatment { font-size: 10.5px; border-bottom-width: 3px; padding-bottom: 2px; }
  .ad-small .price { font-size: 26px; margin-top: 2px; }
  .ad-small .contact-phone { left: 0; right: 110px; top: 279px; font-size: 12px; }
  .ad-small .contact-address { left: 0; right: 110px; top: 297px; font-size: 8px; }
</style>
</head>
<body>
<svg width="0" height="0" style="position:absolute" aria-hidden="true">
  <defs>
    <symbol id="card-frame" viewBox="0 0 100 100" preserveAspectRatio="none">
      <path d="M9 1 H91 A8 8 0 0 0 99 9 V91 A8 8 0 0 0 91 99 H9 A8 8 0 0 0 1 91 V9 A8 8 0 0 0 9 1 Z"
            fill="var(--card-line)" opacity="0.35" vector-effect="non-scaling-stroke"/>
      <path d="M10 3 H90 A7 7 0 0 0 97 10 V90 A7 7 0 0 0 90 97 H10 A7 7 0 0 0 3 90 V10 A7 7 0 0 0 10 3 Z"
            fill="var(--card-fill)" stroke="var(--card-line)" stroke-width="1.5" vector-effect="non-scaling-stroke"/>
      <path d="M12 6 H88 A6 6 0 0 0 94 12 V88 A6 6 0 0 0 88 94 H12 A6 6 0 0 0 6 88 V12 A6 6 0 0 0 12 6 Z"
            fill="none" stroke="var(--card-line)" stroke-width="1" vector-effect="non-scaling-stroke"/>
    </symbol>
  </defs>
</svg>

<main class="stage">
  <span class="size-label" style="left:306px;top:99px">504 x 1200</span>
  <span class="size-label" style="left:853px;top:138px">600 x 600</span>
  <span class="size-label" style="left:852px;top:716px">400 x 400</span>

  <!-- Tall format -->
  <section class="ad ad-tall">
    <div class="header-band"></div>
    <h1 class="brand-title"><span class="brand-line">Brellmoor Cosmetic</span><span class="brand-line">Doctor</span></h1>
    <div class="model-photo" role="img" aria-label="Photo of a young woman with fair skin and hair pulled back, resting her chin on her hands"></div>
    <p class="offer-text"><span>We only use premium products from Velmira,</span><span>offering a free consultation with a doctor</span></p>
    <p class="prices-heading">Prices:</p>
    <div class="price-card" style="left:41px;top:590px;width:153px;height:142px"><svg class="card-frame"><use href="#card-frame"/></svg><span class="treatment">Forehead</span><span class="price">$58</span></div>
    <div class="price-card" style="left:209px;top:590px;width:154px;height:142px"><svg class="card-frame"><use href="#card-frame"/></svg><span class="treatment">Frown lines</span><span class="price">$116</span></div>
    <div class="price-card" style="left:41px;top:746px;width:153px;height:144px"><svg class="card-frame"><use href="#card-frame"/></svg><span class="treatment">Crows feet</span><span class="price">$116</span></div>
    <div class="price-card" style="left:209px;top:746px;width:154px;height:144px"><svg class="card-frame"><use href="#card-frame"/></svg><span class="treatment">Lip fillers</span><span class="price">$380</span></div>
    <p class="contact-phone">0400 559 271</p>
    <p class="contact-address">41 Harlow Street Eastbrook</p>
  </section>

  <!-- Medium square -->
  <section class="ad ad-medium">
    <div class="model-photo" role="img" aria-label="Close-up photo of a young woman with fair skin, hand raised to her jaw"></div>
    <h1 class="brand-title"><span class="brand-line">Brellmoor Cosmetic</span><span class="brand-line">Doctor</span></h1>
    <p class="offer-text">We only use premium products from Velmira,<br>offering a free consultation with a doctor</p>
    <p class="prices-heading">Prices:</p>
    <div class="price-card" style="left:29px;top:156px;width:132px;height:122px"><svg class="card-frame"><use href="#card-frame"/></svg><span class="treatment">Forehead</span><span class="price">$58</span></div>
    <div class="price-card" style="left:173px;top:156px;width:132px;height:122px"><svg class="card-frame"><use href="#card-frame"/></svg><span class="treatment">Frown lines</span><span class="price">$116</span></div>
    <div class="price-card" style="left:29px;top:291px;width:132px;height:119px"><svg class="card-frame"><use href="#card-frame"/></svg><span class="treatment">Crows feet</span><span class="price">$116</span></div>
    <div class="price-card" style="left:173px;top:291px;width:132px;height:119px"><svg class="card-frame"><use href="#card-frame"/></svg><span class="treatment">Lip fillers</span><span class="price">$380</span></div>
    <p class="contact-phone">0400 559 271</p>
    <p class="contact-address">41 Harlow Street Eastbrook</p>
  </section>

  <!-- Small square -->
  <section class="ad ad-small">
    <div class="model-photo" role="img" aria-label="Close-up photo of a young woman with fair skin, hand raised to her jaw"></div>
    <h1 class="brand-title"><span class="brand-line">Brellmoor Cosmetic</span><span class="brand-line">Doctor</span></h1>
    <p class="offer-text">Premium products from Velmira,<br>free consultation with a doctor.</p>
    <p class="prices-heading">Prices:</p>
    <div class="price-card" style="left:21px;top:107px;width:86px;height:79px"><svg class="card-frame"><use href="#card-frame"/></svg><span class="treatment">Forehead</span><span class="price">$58</span></div>
    <div class="price-card" style="left:117px;top:107px;width:86px;height:79px"><svg class="card-frame"><use href="#card-frame"/></svg><span class="treatment">Frown lines</span><span class="price">$116</span></div>
    <div class="price-card" style="left:21px;top:196px;width:86px;height:79px"><svg class="card-frame"><use href="#card-frame"/></svg><span class="treatment">Crows feet</span><span class="price">$116</span></div>
    <div class="price-card" style="left:117px;top:196px;width:86px;height:79px"><svg class="card-frame"><use href="#card-frame"/></svg><span class="treatment">Lip fillers</span><span class="price">$380</span></div>
    <p class="contact-phone">0400 559 271</p>
    <p class="contact-address">41 Harlow Street Eastbrook</p>
  </section>
</main>
</body>
</html>
```